Microlight Aircraft Website Project

Need a website designed, or at least a template made, that my web programmer can work with here. We are a new manufacturer of microlight aircraft & powered hang gliders. Our company name is Brisk Fern. We manufacture portable utility aircraft in the Light Sport category (formerly known as Ultralights or Microlights). Our particular design is a 2-seat powered hang glider and caters to those who want to go explore the backcountry. We are not necessarily aviation nuts, but more into the development of a flying utility vehicle for extreme exploration and expeditions. We have been importing these aircraft from 3 countries for 15 years and have supplied over 200 expedition-quality aircraft world-wide. We are now manufacturing here in the US.

Industry/Entity Type

Manufacturer

Coding

Coded - Design and coding required

```html
<!DOCTYPE html>
<html lang="en">
<head>
<meta charset="utf-8">
<title>Brisk Fern — Microlight Aircraft &amp; Powered Hang Gliders</title>
<link href="https://fonts.googleapis.com/css2?family=Lato:wght@300;400;700;900&display=swap" rel="stylesheet">
<style>
:root{
  --navy:#1b2a4a;
  --blue:#3a4fa3;
  --ink:#2b2f36;
  --muted:#9aa0a8;
  --line:#e3e5e8;
  --paper:#ffffff;
  --soft:#f4f5f6;
  --dark:#1f2328;
  --darker:#17191c;
  --white:#ffffff;
}
*{box-sizing:border-box;margin:0;padding:0}
html,body{width:1200px;height:3789px;overflow:hidden}
body{font-family:'Lato',sans-serif;color:var(--ink);background:var(--paper);position:relative}
section,header,footer{position:absolute;left:0;width:1200px}
.abs{position:absolute}
.container{position:absolute;left:172px;width:856px}

/* header / hero */
.hero{top:0;height:576px;background:linear-gradient(180deg,#5d6e80 0%,#3c4c63 35%,#1e2d47 75%,#142039 100%)}
.hero-photo{position:absolute;inset:0;background:radial-gradient(ellipse at 70% 20%,rgba(190,200,210,.55),rgba(0,0,0,0) 55%),linear-gradient(200deg,rgba(0,0,0,0) 40%,rgba(12,24,44,.6) 100%)}
.brand{position:absolute;left:182px;top:18px;color:var(--white);font-weight:700;font-size:15px;letter-spacing:2px;display:flex;align-items:center;gap:10px}
.brand .mark{width:14px;height:14px;border:2px solid var(--white);border-radius:50%}
.nav{position:absolute;left:380px;top:22px;display:flex;gap:26px;font-size:12px;font-weight:700;letter-spacing:.5px;color:var(--white)}
.nav a{color:var(--white);text-decoration:none;padding-bottom:6px}
.nav a.active{border-bottom:2px solid var(--white)}
.nav-icons{position:absolute;left:955px;top:18px;display:flex;gap:30px}
.hero h1{position:absolute;left:192px;top:205px;color:var(--white);font-weight:900;font-size:56px;line-height:66px;letter-spacing:1px}
.hero .tagline{position:absolute;left:192px;top:352px;color:var(--white);font-size:12px;font-weight:700;letter-spacing:2.5px}
.hero .rule{position:absolute;left:192px;top:402px;width:76px;height:3px;background:var(--blue)}
.hero p{position:absolute;left:192px;top:432px;width:430px;color:#c9d0da;font-size:12px;line-height:16px}

/* features */
.features{top:576px;height:232px;background:var(--paper)}
.feature{position:absolute;top:48px;width:200px}
.feature .head{display:flex;align-items:flex-start;gap:10px}
.feature h3{font-size:11px;font-weight:700;letter-spacing:.6px;color:var(--ink);margin-top:4px}
.feature p{margin-left:50px;margin-top:2px;font-size:10px;line-height:15px;color:var(--muted);width:140px}
.feature .more{display:block;margin-left:50px;margin-top:16px;font-size:10px;font-weight:700;color:var(--blue);letter-spacing:.6px}

/* about */
.about{top:808px;height:538px;background:linear-gradient(90deg,#f2f4f5 0%,#e9eef0 45%,#b8c9d2 65%,#7f9a86 85%,#5c7a5f 100%)}
.eyebrow{position:absolute;left:182px;top:92px;font-size:10px;letter-spacing:3px;color:var(--blue);font-weight:700}
.about h2{position:absolute;left:182px;top:132px;width:560px;font-weight:400;font-size:29px;line-height:40px;color:var(--ink)}
.about p{position:absolute;left:182px;top:243px;width:545px;font-size:11px;line-height:17px;color:#555b63}
.btn{position:absolute;background:var(--blue);color:var(--white);font-size:12px;display:flex;align-items:center;justify-content:center}

/* section heading */
.sec-title{position:absolute;left:0;width:1200px;text-align:center;font-weight:300;font-size:32px;color:var(--ink)}
.sec-sub{position:absolute;left:400px;width:400px;text-align:center;font-size:11px;line-height:16px;color:var(--muted)}
.sec-rule{position:absolute;left:562px;width:76px;height:3px;background:var(--blue)}

/* products */
.products{top:1346px;height:531px;background:var(--paper)}
.product{position:absolute;top:202px;width:270px}
.product .frame{height:190px;border:1px solid var(--line);padding:10px}
.product .shot{width:100%;height:100%;background:linear-gradient(180deg,#f7f7f8,#e5e7ea)}
.product h3{margin-top:20px;font-weight:400;font-size:18px;color:var(--ink);padding-left:8px}
.product p{margin-top:8px;padding-left:8px;font-size:10px;line-height:14px;color:var(--muted)}

/* contact */
.contact{top:1877px;height:480px;background:var(--soft)}
.contact h2{position:absolute;left:182px;top:52px;font-weight:400;font-size:30px;color:var(--ink)}
.contact .sub{position:absolute;left:182px;top:98px;width:380px;font-size:11px;line-height:16px;color:var(--muted)}
.contact .rule{position:absolute;left:182px;top:157px;width:76px;height:3px;background:var(--blue)}
.field{position:absolute;left:182px;width:380px;height:24px;background:var(--paper);border:1px solid var(--line);font-size:10px;color:var(--muted);padding:6px 8px}
.field.area{height:72px}
.contact-photo{position:absolute;left:590px;top:131px;width:598px;height:253px;background:radial-gradient(ellipse at 50% 50%,#d33a3a 0%,#b02a2a 25%,rgba(240,240,242,0) 60%)}

/* stats band */
.stats{top:2357px;height:257px;background:linear-gradient(180deg,#3c4f6b 0%,#54677c 40%,#3f5a3c 75%,#2c4329 100%)}
.stats p{position:absolute;left:0;width:1200px;top:70px;text-align:center;color:var(--white);font-weight:300;font-size:28px;line-height:36px}
.btn-ghost{position:absolute;left:518px;top:164px;width:164px;height:40px;border:1px solid rgba(255,255,255,.8);color:var(--white);font-size:18px;display:flex;align-items:center;justify-content:center;font-weight:300}

/* partners */
.partners{top:2614px;height:205px;background:var(--dark)}
.partner{position:absolute;top:90px;font-size:19px;font-weight:700;color:#3d4249;display:flex;align-items:center;gap:10px}
.partner .dot{width:22px;height:22px;background:#3d4249}

/* posts */
.posts{top:2819px;height:606px;background:var(--soft)}
.post{position:absolute;top:200px;width:270px;height:361px;background:var(--paper)}
.post .thumb{height:146px}
.post .body{padding:24px 44px 0 44px}
.post .date{font-size:10px;font-weight:700;letter-spacing:.5px;color:var(--ink)}
.post h3{margin-top:12px;font-weight:400;font-size:14px;color:var(--ink)}
.post p{margin-top:8px;font-size:10px;line-height:14px;color:var(--muted)}
.post .more{display:flex;align-items:center;gap:6px;margin-top:20px;font-size:10px;font-weight:700;color:var(--blue);letter-spacing:.5px}

/* footer */
.footer{top:3425px;height:364px;background:var(--darker);color:#8d939b}
.footer .brand{top:76px;left:182px}
.addr{position:absolute;left:182px;top:180px;font-size:10px;line-height:16px}
.addr div{display:flex;gap:10px;margin-bottom:6px}
.social{position:absolute;left:182px;top:286px;display:flex;gap:18px}
.fcol{position:absolute;top:78px;width:190px}
.fcol h4{font-weight:400;font-size:17px;color:var(--white);margin-bottom:18px}
.fcol p{font-size:10px;line-height:14px}
.fcol .d{color:var(--blue);font-size:9px;margin-bottom:14px;margin-top:2px}
.nl-input{width:188px;height:20px;border:1px solid #3a3f46;font-size:9px;padding:4px 6px;margin-top:8px;color:#6d737b}
.nl-btn{width:54px;height:18px;background:var(--blue);color:var(--white);font-size:9px;display:flex;align-items:center;justify-content:center;margin-top:8px}
.widget{position:absolute;left:829px;top:73px;width:199px;height:190px;background:var(--paper);border:1px solid #ccc}
.bottom{position:absolute;left:0;top:301px;width:1200px;height:63px;border-top:1px solid #2a2e33}
.bottom .copy{position:absolute;left:182px;top:26px;font-size:10px;color:#c5cad1}
.bottom .links{position:absolute;left:776px;top:26px;display:flex;gap:30px;font-size:10px;color:#c5cad1}
</style>
</head>
<body>

<header class="hero">
  <div class="hero-photo" role="img" aria-label="Misty forested mountains with a powered hang glider flying overhead"></div>
  <div class="brand"><span class="mark"></span>BRISK FERN</div>
  <nav class="nav">
    <a class="active">HOME</a><a>ABOUT</a><a>SERVICE</a><a>PRODUCTS</a><a>MY ACCOUNT</a><a>CONTACT</a>
  </nav>
  <div class="nav-icons">
    <svg width="14" height="14" viewBox="0 0 14 14"><circle cx="6" cy="6" r="4.5" fill="none" stroke="#fff" stroke-width="1.8"/><line x1="9.5" y1="9.5" x2="13" y2="13" stroke="#fff" stroke-width="1.8"/></svg>
    <svg width="14" height="14" viewBox="0 0 14 14"><rect x="2" y="3" width="10" height="1.6" fill="#fff"/><rect x="2" y="6.2" width="10" height="1.6" fill="#fff"/><rect x="2" y="9.4" width="10" height="1.6" fill="#fff"/></svg>
  </div>
  <h1>DON’T LIMIT<br>YOURSELF</h1>
  <div class="tagline">EXTREME EXPLORATION AND EXPEDITIONS</div>
  <div class="rule"></div>
  <p>Sed ut perspiciatis unde omnis iste natus error sit voluptatem accusantium doloremque laudantium, totam rem aperiam, eaque ipsa quae</p>
</header>

<section class="features">
  <div class="feature" style="left:177px">
    <div class="head"><svg width="40" height="30" viewBox="0 0 40 30"><polyline points="4,24 12,14 20,18 34,4" fill="none" stroke="#3a4fa3" stroke-width="2"/><line x1="2" y1="27" x2="38" y2="27" stroke="#3a4fa3" stroke-width="1.5"/></svg><h3>15 YEARS EXPERIENCE</h3></div>
    <p>Sed quia consequuntur magni dolores eos qui ratione voluptatem sequi nesciunt.</p>
    <span class="more">READ MORE</span>
  </div>
  <div class="feature" style="left:392px">
    <div class="head"><svg width="40" height="30" viewBox="0 0 40 30"><circle cx="20" cy="12" r="9" fill="none" stroke="#3a4fa3" stroke-width="2"/><polyline points="14,19 12,29 20,25 28,29 26,19" fill="none" stroke="#3a4fa3" stroke-width="2"/></svg><h3>QUALITY PRODUCT</h3></div>
    <p>Neque porro quisquam est qui dolorem ipsum quia dolor sit amet consequuntur magni.</p>
    <span class="more">READ MORE</span>
  </div>
  <div class="feature" style="left:611px">
    <div class="head"><svg width="40" height="30" viewBox="0 0 40 30"><circle cx="20" cy="15" r="12" fill="none" stroke="#3a4fa3" stroke-width="2"/><text x="20" y="20" text-anchor="middle" font-size="14" font-family="Lato,sans-serif" fill="#3a4fa3">$</text></svg><h3>UNBEATABLE VALUE</h3></div>
    <p>Sed quia consequuntur magni dolores eos qui ratione voluptatem sequi nesciunt.</p>
    <span class="more">READ MORE</span>
  </div>
  <div class="feature" style="left:834px">
    <div class="head"><svg width="40" height="30" viewBox="0 0 40 30"><rect x="3" y="8" width="20" height="14" fill="none" stroke="#3a4fa3" stroke-width="2"/><polyline points="23,12 31,12 36,17 36,22 23,22" fill="none" stroke="#3a4fa3" stroke-width="2"/><circle cx="10" cy="24" r="3" fill="#fff" stroke="#3a4fa3" stroke-width="2"/><circle cx="30" cy="24" r="3" fill="#fff" stroke="#3a4fa3" stroke-width="2"/></svg><h3>WORLD WIDE DELIVERY</h3></div>
    <p>Neque porro quisquam est qui dolorem ipsum quia dolor sit amet consequuntur magni.</p>
    <span class="more">READ MORE</span>
  </div>
</section>

<section class="about" role="img" aria-label="Pilot flying a powered hang glider over green forested hills">
  <div class="eyebrow">UT ENIM AD MINIMA VENIAM, QUIS NOSTRUM EXERCITATIONEM</div>
  <h2>We are a new manufacturer of microlight aircraft &amp; powered hang gliders</h2>
  <p>In et massa a massa egestas suscipit tincidunt ut est. Curabitur rutrum faucibus elit, id convallis diam mattis eget. Nullam vulputate nibh at nisi consectetur. Sed ut perspiciatis unde omnis iste natus error sit voluptatem accusantium doloremque laudantium, totam rem aperiam, eaque ipsa quae ab illo inventore veritatis et quasi architecto beatae vitae dicta sunt explicabo. Nemo enim ipsam voluptatem quia voluptas sit aspernatur aut odit aut fugit, sed quia consequuntur magni dolores eos qui ratione voluptatem sequi nesciunt. Neque porro quisquam est, qui dolorem ipsum quia dolor sit amet, consectetur, adipisci velit, sed quia non numquam eius modi tempora incidunt ut labore et dolore magnam aliquam quaerat voluptatem.</p>
  <div class="btn" style="left:182px;top:437px;width:114px;height:36px">Read More</div>
</section>

<section class="products">
  <div class="sec-title" style="top:50px">Our Products</div>
  <div class="sec-sub" style="top:98px">Perspiciatis unde omnis iste natus error sit voluptatem accusantium doloremque laudantium, totam rem aperiam, eaque ipsa quae</div>
  <div class="sec-rule" style="top:148px"></div>
  <div class="product" style="left:172px">
    <div class="frame"><div class="shot" role="img" aria-label="Microlight aircraft with dark wing on white background"></div></div>
    <h3>Microlight aircraft</h3>
    <p>Quis autem vel eum iure reprehenderit qui in ea voluptate velit esse quam nihil molestiae consequatur, vel illum qui dolorem eum fugiat quo voluptas.</p>
  </div>
  <div class="product" style="left:465px">
    <div class="frame"><div class="shot" role="img" aria-label="Powered hang glider trike on white background"></div></div>
    <h3>Powered hang gliders</h3>
    <p>At vero eos et accusamus et iusto odio dignissimos ducimus qui blanditiis praesentium voluptatum deleniti atque corrupti quos dolores.</p>
  </div>
  <div class="product" style="left:758px">
    <div class="frame"><div class="shot" role="img" aria-label="Two-seat powered hang glider on white background"></div></div>
    <h3>2-seat powered hang glider</h3>
    <p>Nam libero tempore, cum soluta nobis est eligendi optio cumque nihil impedit quo minus id quod maxime placeat facere possimus omnis.</p>
  </div>
</section>

<section class="contact">
  <h2>Get In touch</h2>
  <div class="sub">Perspiciatis unde omnis iste natus error sit voluptatem accusantium doloremque laudantium, totam rem aperiam, eaque ipsa quae</div>
  <div class="rule"></div>
  <div class="field" style="top:212px">Name</div>
  <div class="field" style="top:248px">Email</div>
  <div class="field" style="top:284px">Phone No</div>
  <div class="field area" style="top:320px">Your Message</div>
  <div class="btn" style="left:182px;top:394px;width:86px;height:28px;font-size:10px">Sign Up now</div>
  <div class="contact-photo" role="img" aria-label="Red and white powered hang glider trike"></div>
</section>

<section class="stats" role="img" aria-label="Wide valley landscape with green hills under a cloudy sky">
  <p>We have supplied over 200 expedition-quality aircraft<br>world-wide for 15 years.</p>
  <div class="btn-ghost">Order now</div>
</section>

<section class="partners">
  <div class="partner" style="left:182px"><span class="dot"></span>Marrow Group</div>
  <div class="partner" style="left:380px">Cedar Hollow</div>
  <div class="partner" style="left:545px">Brightmill</div>
  <div class="partner" style="left:700px"><span class="dot" style="border-radius:50%"></span>Ridgeway</div>
  <div class="partner" style="left:880px">Stonelark</div>
</section>

<section class="posts">
  <div class="sec-title" style="top:45px">Recent Posts</div>
  <div class="sec-sub" style="top:94px">Perspiciatis unde omnis iste natus error sit voluptatem accusantium doloremque laudantium, totam rem aperiam, eaque ipsa quae</div>
  <div class="sec-rule" style="top:157px"></div>
  <div class="post" style="left:172px">
    <div class="thumb" role="img" aria-label="Yellow microlight aircraft parked on a snowy airfield" style="background:linear-gradient(180deg,#a9c3e0,#e8e6dc)"></div>
    <div class="body"><div class="date">MAY 02, 2016</div><h3>Sed ut perspiciatis unde</h3><p>Vitae dicta sunt explicabo. Nemo enim ipsam voluptatem quia voluptas sit aspernatur aut odit aut fugit sed quia consequuntur...</p><div class="more">READ MORE <span>→</span></div></div>
  </div>
  <div class="post" style="left:465px">
    <div class="thumb" role="img" aria-label="Powered hang glider flying above a blue lake" style="background:linear-gradient(180deg,#7fa9d6,#3d6e9a)"></div>
    <div class="body"><div class="date">APRIL 28, 2016</div><h3>Quis autem vel eum iure</h3><p>Eum dicta sunt explicabo. Nemo enim ipsam voluptatem quia voluptas sit aspernatur adodip incl velit, sed quia non numquam eius modi...</p><div class="more">READ MORE <span>→</span></div></div>
  </div>
  <div class="post" style="left:758px">
    <div class="thumb" role="img" aria-label="Hang glider soaring over a green valley" style="background:linear-gradient(180deg,#8fb4c9,#6f9a6a)"></div>
    <div class="body"><div class="date">APRIL 15, 2016</div><h3>Veritatis et quasi arch</h3><p>Numquam eius modi tempora incidunt ut labore et dolore magnam aliquam quaerat voluptatem. Ut enim ad minima veniam, quis nostrud...</p><div class="more">READ MORE <span>→</span></div></div>
  </div>
</section>

<footer class="footer">
  <div class="brand"><span class="mark"></span>BRISK FERN</div>
  <div class="addr">
    <div><svg width="10" height="12" viewBox="0 0 10 12"><path d="M5 1a3.5 3.5 0 0 1 3.5 3.5C8.5 7 5 11 5 11S1.5 7 1.5 4.5A3.5 3.5 0 0 1 5 1z" fill="#3a4fa3"/></svg><span>418 Alder Lane<br>Pine Hollow, IL 60000</span></div>
    <div><svg width="10" height="12" viewBox="0 0 10 12"><path d="M2 1h2l1 3-1.5 1a6 6 0 0 0 2.5 2.5L7 6l3 1v2a1 1 0 0 1-1 1A8 8 0 0 1 1 2a1 1 0 0 1 1-1z" fill="#3a4fa3"/></svg><span>+1 555 010 2288</span></div>
    <div><svg width="10" height="12" viewBox="0 0 10 12"><rect x="0.5" y="3" width="9" height="6.5" fill="none" stroke="#3a4fa3"/><polyline points="0.5,3 5,7 9.5,3" fill="none" stroke="#3a4fa3"/></svg><span>info@briskfern.com</span></div>
  </div>
  <div class="social">
    <svg width="8" height="8"><circle cx="4" cy="4" r="3" fill="#8d939b"/></svg>
    <svg width="8" height="8"><circle cx="4" cy="4" r="3" fill="#8d939b"/></svg>
    <svg width="8" height="8"><circle cx="4" cy="4" r="3" fill="#8d939b"/></svg>
  </div>
  <div class="fcol" style="left:399px">
    <h4>Latest News</h4>
    <p>Similique sunt in culpa qui officia deserunt mollitia anim</p><div class="d">15 Mar, 2016</div>
    <p>Culpa qui officia deserunt mollit ha anim idest laborum</p><div class="d">17 Mar, 2016</div>
  </div>
  <div class="fcol" style="left:614px">
    <h4>Newsletter</h4>
    <p>By subscribing to our mailing list you will always be update with the latest news from us.</p>
    <div class="nl-input">Your name...</div>
    <div class="nl-input">Your mail address...</div>
    <div class="nl-btn">SUBMIT</div>
  </div>
  <div class="widget" role="img" aria-label="Social page preview with a hang glider photo and follower thumbnails" style="background:linear-gradient(180deg,#6f93c6 0%,#b8cbe2 55%,#ffffff 56%)"></div>
  <div class="bottom">
    <div class="copy">Copyright © Brisk Fern 2016</div>
    <div class="links"><span>Contact Us</span><span>Site Map</span><span>About Us</span></div>
  </div>
</footer>

</body>
</html>
```